Ridgeline Vale construction brochure

i would like a brochure that can be send to clients digitally and printed. we are a geotechnical, foundation, and concrete company. I attached info below

Target Market(s)

Construction managers, general contractors, developers, municipalities, private, and commercial partners.

Industry/Entity Type

Geotechnical / foundation

Font styles to use
Serif
Other font styles liked:
• Maybe same as logo

Colors
0054AA
0677BA
7BADD7
CADEEF
E8F1F8

```html
<!DOCTYPE html>
<html lang="en">
<head>
<meta charset="utf-8">
<title>Ridgeline Vale – Geotechnical, Foundation &amp; Concrete Brochure</title>
<link href="https://fonts.googleapis.com/css2?family=Poppins:wght@700;800&family=Encode+Sans+Condensed:wght@400;600&display=swap" rel="stylesheet">
<style>
  :root{
    --navy:#253358;
    --orange:#d98a2a;
    --accent-blue:#29a8e0;
    --panel-grey:#e8e9ea;
    --backdrop:#8a8b8a;
    --white:#ffffff;
    --body-text:#3a3f4a;
  }
  *{box-sizing:border-box;margin:0;padding:0}
  html,body{width:1200px;height:1200px;overflow:hidden;background:var(--backdrop)}
  .brochure{position:absolute;left:217px;top:104px;width:766px;height:990px;background:var(--white);overflow:hidden;font-family:"Encode Sans Condensed",sans-serif}

  .hero-art{position:absolute;left:0;top:0;width:766px;height:506px}

  .brand{position:absolute;left:35px;top:36px;height:51px;display:flex;align-items:center;gap:10px;
    font-family:"Poppins",sans-serif;font-weight:700;font-size:30px;letter-spacing:1px;color:var(--navy)}
  .brand-square{width:18px;height:18px;background:var(--navy)}

  .headline{position:absolute;left:35px;top:117px;font-family:"Poppins",sans-serif;font-weight:800;
    font-size:41px;line-height:37px;letter-spacing:.3px;color:var(--navy)}
  .headline .accent{color:var(--orange)}

  .intro{position:absolute;left:35px;top:374px;width:272px;font-size:11.8px;line-height:18px;color:var(--body-text)}

  .tagline-bar{position:absolute;left:382px;top:456px;width:384px;height:50px;display:flex;align-items:center;justify-content:center;
    font-family:"Poppins",sans-serif;font-weight:800;font-size:15.5px;color:var(--white);letter-spacing:.2px;gap:6px}
  .tagline-bar .divider{color:var(--accent-blue)}

  .services{position:absolute;left:0;top:506px;width:766px;height:239px;background:var(--panel-grey)}
  .services-title{position:absolute;left:0;top:21px;width:766px;text-align:center;font-family:"Poppins",sans-serif;font-weight:700;
    font-size:16.5px;color:var(--orange)}
  .services-rule{position:absolute;top:32px;height:1px;background:var(--orange)}
  .service-icon{position:absolute;top:52px;width:58px;height:58px}
  .service-name{position:absolute;top:62px;font-family:"Poppins",sans-serif;font-weight:800;font-size:14.5px;line-height:16px;color:var(--navy)}
  .service-list{position:absolute;list-style:none;font-weight:600;font-size:12.3px;color:var(--navy)}
  .service-list li{height:21.1px;line-height:21.1px;position:relative;padding-left:17px}
  .service-list li::before{content:"";position:absolute;left:0;top:8px;width:5px;height:5px;border-radius:50%;background:var(--orange)}

  .photo-round{position:absolute;top:776px;width:140px;height:140px}
  .why-title{position:absolute;left:0;top:778px;width:766px;text-align:center;font-family:"Poppins",sans-serif;font-weight:800;font-size:16.5px;color:var(--navy)}
  .why-text{position:absolute;left:158px;top:807px;width:450px;text-align:center;font-size:11.8px;line-height:18px;color:var(--body-text)}
  .cta{position:absolute;left:0;top:914px;width:766px;text-align:center;font-family:"Poppins",sans-serif;font-weight:800;font-size:16.5px;color:var(--orange)}

  .footer{position:absolute;left:0;top:943px;width:766px;height:47px;background:var(--navy);display:flex;align-items:center;justify-content:center;
    font-family:"Poppins",sans-serif;font-weight:700;font-size:17px;color:var(--white)}
</style>
</head>
<body>
<main class="brochure">

  <svg class="hero-art" viewBox="0 0 766 506">
    <defs>
      <linearGradient id="site-tones" x1="0" y1="0" x2="0" y2="1">
        <stop offset="0" stop-color="#1e86e8"/>
        <stop offset=".42" stop-color="#7fb6e6"/>
        <stop offset=".55" stop-color="#a99a78"/>
        <stop offset=".75" stop-color="#8e8d88"/>
        <stop offset="1" stop-color="#6d6a63"/>
      </linearGradient>
    </defs>
    <polygon points="300,506 416,0 421,0 306,506" fill="var(--orange)"/>
    <polygon points="429,0 766,0 766,506 311,506" fill="url(#site-tones)" role="img" aria-label="Photo of workers levelling a concrete pour over rebar mesh with pump booms and formwork columns on a construction site"/>
    <polygon points="370,456 766,456 766,506 355,506" fill="var(--navy)"/>
  </svg>

  <div class="brand"><span class="brand-square"></span>RIDGELINE VALE</div>

  <h1 class="headline">BUILDING<br>STRONG<br>FOUNDATIONS.<br><span class="accent">DELIVERING<br>LASTING<br>SOLUTIONS.</span></h1>

  <p class="intro">At Ridgeline Vale, we provide dependable geotechnical, foundation, and concrete solutions for commercial, industrial, and infrastructure projects. Our experienced team combines technical expertise, advanced equipment, and a commitment to quality to help clients build with confidence—from initial site investigation through project completion.</p>

  <div class="tagline-bar">GEOTECHNICAL <span class="divider">|</span> FOUNDATION <span class="divider">|</span> CONCRETE</div>

  <section class="services">
    <div class="services-rule" style="left:35px;width:250px"></div>
    <h2 class="services-title">OUR CORE SERVICES</h2>
    <div class="services-rule" style="left:481px;width:248px"></div>

    <svg class="service-icon" style="left:36px" viewBox="0 0 58 58" role="img" aria-label="Geotechnical icon">
      <circle cx="29" cy="29" r="29" fill="var(--navy)"/>
      <g fill="none" stroke="var(--orange)" stroke-width="1.6">
        <rect x="17" y="16" width="10" height="20"/><rect x="27" y="22" width="9" height="14"/>
        <line x1="42" y1="14" x2="42" y2="34"/><circle cx="42" cy="13" r="2"/>
        <path d="M15 38 h28 M20 38 a9 7 0 0 0 18 0"/>
      </g>
    </svg>
    <h3 class="service-name" style="left:104px">GEOTECHNICAL<br>SERVICES</h3>
    <ul class="service-list" style="left:104px;top:104px">
      <li>Site Investigation</li><li>Soil Exploration &amp; Sampling</li><li>Subsurface Testing</li>
      <li>Geotechnical Engineering</li><li>Foundation Recommendations</li><li>Construction Materials Testing</li>
    </ul>

    <svg class="service-icon" style="left:275px" viewBox="0 0 58 58" role="img" aria-label="Foundation piles icon">
      <circle cx="29" cy="29" r="29" fill="var(--navy)"/>
      <g fill="none" stroke="var(--orange)" stroke-width="1.6">
        <rect x="18" y="12" width="4" height="22"/><rect x="36" y="12" width="4" height="22"/>
        <path d="M14 34 h30 v8 h-30 z"/><line x1="16" y1="38" x2="42" y2="38"/>
      </g>
    </svg>
    <h3 class="service-name" style="left:344px">FOUNDATION<br>SERVICES</h3>
    <ul class="service-list" style="left:344px;top:104px">
      <li>Deep Foundations</li><li>Drilled Shafts</li><li>Helical Piers</li>
      <li>Micropiles</li><li>Driven Piles</li><li>Ground Improvement</li>
    </ul>

    <svg class="service-icon" style="left:500px" viewBox="0 0 58 58" role="img" aria-label="Concrete mixer truck icon">
      <circle cx="29" cy="29" r="29" fill="var(--navy)"/>
      <g fill="none" stroke="var(--orange)" stroke-width="1.8">
        <path d="M12 36 v-10 l14 -8 h8 v18 z"/><path d="M34 24 h7 l5 6 v6 h-12"/>
        <circle cx="19" cy="38" r="3"/><circle cx="40" cy="38" r="3"/>
      </g>
    </svg>
    <h3 class="service-name" style="left:570px">CONCRETE<br>SERVICES</h3>
    <ul class="service-list" style="left:570px;top:101px">
      <li>Structural Concrete</li><li>Foundations &amp; Footings</li><li>Slabs-on-Grade</li>
      <li>Retaining Walls</li><li>Equipment Foundations</li><li>Industrial Concrete</li>
    </ul>
  </section>

  <svg class="photo-round" style="left:15px" viewBox="0 0 140 140" role="img" aria-label="Photo of site crew in hard hats and safety vests reviewing a building under construction">
    <defs><linearGradient id="crew-tones" x1="0" y1="0" x2="0" y2="1"><stop offset="0" stop-color="#7dbde0"/><stop offset=".55" stop-color="#b9c3c4"/><stop offset="1" stop-color="#b88a4a"/></linearGradient></defs>
    <circle cx="70" cy="70" r="70" fill="url(#crew-tones)"/>
  </svg>
  <svg class="photo-round" style="left:611px" viewBox="0 0 140 140" role="img" aria-label="Photo of a mixer truck chute pouring concrete onto rebar mesh">
    <defs><linearGradient id="pour-tones" x1="0" y1="0" x2="0" y2="1"><stop offset="0" stop-color="#4f6b3c"/><stop offset=".5" stop-color="#b9b7b1"/><stop offset="1" stop-color="#c0712e"/></linearGradient></defs>
    <circle cx="70" cy="70" r="70" fill="url(#pour-tones)"/>
  </svg>

  <h2 class="why-title">WHY CHOOSE RIDGELINE VALE?</h2>
  <p class="why-text">Experienced ProfessionalsOur team brings years of field experience across a wide range of commercial and heavy civil projects.Safety FocusedSafety is integrated into every phase of our work, protecting our employees, clients, and project sites.Reliable PerformanceWe understand the importance of schedules and deliver dependable solutions that minimize delays.Quality You Can TrustEvery project is completed with attention to detail, precision, and industry best practices.</p>
  <p class="cta">LET'S BUILD SOMETHING STRONG TOGETHER</p>

  <footer class="footer">www.ridgelinevale.com</footer>
</main>
</body>
</html>
```